Self help book from Lantern Path needs awesome cover

We need a paperback and e-book cover for a self help book that is about to be published. The title is 'Quiet Harbor Awaits Wanderer: Channel Restless Hunger Toward Purpose'. Synopsis: Future You has achieved great success, and is trying to get an urgent communication to Present You to tell you how to master your mind and life so that you can achieve that greatness. If you don’t, the future won’t happen like it can, or should. Your destiny is to really make a difference in the lives of all of us. It’s not just for you. There are practical things you can do to think more clearly, and some mindfulness exercises to hone your skills. We currently do not have any color or graphic preferences, we're excited to see what you come up with! The final cover should express clarity, confidence, and a bit of urgency. Author's name is Marcus Pellow. Author name should be at the bottom.

```html
<!DOCTYPE html>
<html lang="en">
<head>
<meta charset="utf-8">
<title>Quiet Harbor Awaits Wanderer — Marcus Pellow</title>
<link rel="stylesheet" href="https://fonts.googleapis.com/css2?family=Anton&family=Arimo&family=Libre+Baskerville&display=swap">
<style>
  :root {
    --backdrop: #e9e9e8;
    --paper: #ffffff;
    --navy: #0c2257;
    --ink: #111111;
    --author-red: #e0101e;
    --bulb-gold: #f5b400;
    --bulb-light: #fde7a0;
  }
  * { margin: 0; padding: 0; box-sizing: border-box; }
  html, body {
    width: 1200px;
    height: 800px;
    overflow: hidden;
    background: var(--backdrop);
  }
  .canvas {
    position: relative;
    width: 1200px;
    height: 800px;
    display: flex;
    align-items: center;
    justify-content: center;
  }
  .cover {
    position: relative;
    width: 507px;
    height: 760px;
    background: var(--paper);
    box-shadow: 0 2px 10px rgba(0,0,0,0.12);
  }
  .cover__emblem {
    position: absolute;
    top: 37px;
    left: 50%;
    width: 155px;
    height: 150px;
    transform: translateX(-50%);
    border-radius: 50%;
    background: radial-gradient(circle at 50% 50%, var(--bulb-light) 0%, var(--bulb-gold) 75%, rgba(245,180,0,0) 100%);
  }
  .cover__title {
    position: absolute;
    top: 196px;
    left: 0;
    right: 0;
    text-align: center;
    font-family: "Anton", "Arial Narrow", sans-serif;
    font-size: 74px;
    line-height: 85px;
    color: var(--navy);
    text-transform: uppercase;
    letter-spacing: 0.5px;
  }
  .cover__title span { display: block; }
  .cover__subtitle {
    position: absolute;
    top: 554px;
    left: 0;
    right: 0;
    text-align: center;
    font-family: "Arimo", Arial, sans-serif;
    font-size: 22px;
    line-height: 29px;
    color: var(--ink);
    text-transform: uppercase;
  }
  .cover__author {
    position: absolute;
    top: 682px;
    left: 0;
    right: 0;
    text-align: center;
    font-family: "Libre Baskerville", "Times New Roman", serif;
    font-size: 36px;
    letter-spacing: 7px;
    color: var(--author-red);
    text-transform: uppercase;
  }
</style>
</head>
<body>
  <main class="canvas">
    <article class="cover">
      <div class="cover__emblem" role="img" aria-label="Hand-drawn glowing yellow light bulb with radiating rays"></div>
      <h1 class="cover__title">
        <span>Quiet</span>
        <span>Harbor</span>
        <span>Awaits</span>
        <span>Wanderer</span>
      </h1>
      <p class="cover__subtitle">Channel Restless Hunger<br>Toward Purpose'. Synopsis</p>
      <p class="cover__author">Marcus Pellow</p>
    </article>
  </main>
</body>
</html>
```